Old Mills Along the Whitebrook Vale

We need a cover for a regional book "Die Mühlen am Weißen Bach". The book is about the region frankonia in southern Germany and about the history of electricity in from 1900 to now. The cover should have some regional reference and some reference to electric power. It contains history and stories about electricity.

Reason: We have to wait for the opinion of the publisher.

Target Market(s)

Adults based in southern Germany who are interested in local history and electricity

Requirements
Must have
• Regional reference to franconia (Region in southern Germany) and reference to electricity.
Nice to have
• The files are just some examples for regional pictures, they are not necessary.

```html
<!DOCTYPE html>
<html lang="de">
<head>
<meta charset="utf-8">
<title>Die Mühlen am Weißen Bach – Buchcover</title>
<link rel="stylesheet" href="https://fonts.googleapis.com/css2?family=Lato:wght@300;400;700;900&family=Raleway:wght@500;600&display=swap">
<style>
  :root {
    --stage: #e4e4e4;
    --franconian-red: #e3262f;
    --franconian-red-deep: #c81d26;
    --paper-top: #f4f4f5;
    --paper-bottom: #dcdce0;
    --text-grey: #8c8c90;
    --author-grey: #6d6d71;
    --accent-red: #9b0f12;
    --figure-grey: #77767a;
    --ray-grey: #c9c9cc;
  }
  html, body {
    margin: 0;
    width: 1111px;
    height: 1200px;
    overflow: hidden;
    background: var(--stage);
  }
  .cover {
    position: absolute;
    left: 225px;
    top: 50px;
    width: 660px;
    height: 1100px;
    overflow: hidden;
    background: linear-gradient(180deg, var(--paper-top) 0%, var(--paper-bottom) 100%);
    box-shadow: 0 2px 10px rgba(0,0,0,0.12);
  }
  .banner {
    position: absolute;
    left: 0;
    top: 0;
    width: 660px;
    height: 450px;
  }
  .title {
    position: absolute;
    left: 0;
    right: 0;
    top: 90px;
    margin: 0;
    text-align: center;
    color: #fff;
    font-family: "Raleway", sans-serif;
    font-weight: 600;
    text-transform: uppercase;
    line-height: 1;
  }
  .title-main {
    display: block;
    font-size: 94px;
    letter-spacing: 1px;
  }
  .title-sub {
    display: block;
    margin-top: 22px;
    font-size: 54px;
    letter-spacing: 2px;
  }
  .illustration {
    position: absolute;
    left: 10px;
    top: 540px;
    width: 400px;
    height: 540px;
    background: radial-gradient(ellipse at 45% 40%, var(--figure-grey) 0%, #9a999d 38%, var(--ray-grey) 62%, rgba(220,220,224,0) 80%);
  }
  .subtitle {
    position: absolute;
    right: 40px;
    top: 700px;
    margin: 0;
    text-align: right;
    font-family: "Lato", sans-serif;
    font-weight: 300;
    font-size: 29px;
    line-height: 1.12;
    color: var(--text-grey);
    text-transform: uppercase;
  }
  .subtitle strong {
    font-weight: 900;
    color: var(--accent-red);
    font-size: 31px;
  }
  .tagline {
    position: absolute;
    right: 40px;
    top: 930px;
    margin: 0;
    text-align: right;
    font-family: "Lato", sans-serif;
    font-weight: 300;
    font-size: 20px;
    line-height: 1.12;
    color: var(--text-grey);
    text-transform: uppercase;
  }
  .author {
    position: absolute;
    right: 40px;
    top: 988px;
    margin: 0;
    font-family: "Lato", sans-serif;
    font-weight: 700;
    font-size: 29px;
    color: var(--author-grey);
    text-transform: uppercase;
  }
</style>
</head>
<body>
  <main class="cover">
    <svg class="banner" viewBox="0 0 660 450" aria-hidden="true">
      <polygon fill="var(--franconian-red)"
        points="0,0 660,0 660,450 577.5,365 495,450 412.5,365 330,450 247.5,365 165,450 82.5,365 0,450"/>
    </svg>

    <h1 class="title">
      <span class="title-main">Die Mühlen</span>
      <span class="title-sub">am Weißen Bach</span>
    </h1>

    <div class="illustration" role="img"
         aria-label="Grafische Illustration: kniende Kraftfigur, die einen Blitz schleudert, vor einem Strahlenkranz in Grautönen"></div>

    <p class="subtitle">
      Strom aus<br>
      Wasserkraft - von<br>
      der Kaiserzeit<br>
      bis zur<br>
      <strong>Energiewende</strong>
    </p>

    <p class="tagline">Geschichte,<br>Geschichten und Strom</p>
    <p class="author">von Konrad Weidner</p>
  </main>
</body>
</html>
```